Increased budget: GUI redesign: 10 year old user interface needs modern look-and-feel

UPDATE: Please DO look at more than only th eone image I attached! Almost all designs are simply reworks of that one picture. That is not what we are looking for. Check out the video to understand what the product does, and try to make something better.
We have an existing app (see https://www.vextorane.com/downloadBrivoPanel.php?vers=3_9_1_140964&dir=Vextorane_OEM/3_9_1_140964&name=DSP_Control_Software) which needs refreshing. See also a video here: https://vextorane-oem.com/software/ and the user manual attached here. The GUI is now 800x400 pixels, which is too small; and not scalable, which will be fixed in the future. We need a new, modern look-and-feel, and images that can be exported from the design in various sizes. The current design is attached as well as a collection of PNG files. The overall layout can stay similar, although we are open to good ideas for improvements. The design should be targeted at professional users, not end users; the product is used by audio professionals (e.g. sound engineers, loudspeaker designers). Also see our web version: https://www.vextorane.com/brivopanel/skins/1_1_2/container.html?MAC=Demo%201x2
The winner will also be asked to do a full design of the application GUI (based on the design done here), with several more windows etc, and additional payment depending on the work to be done.

Target Market(s)

Professional audio

Industry/Entity Type

Audio / Industrial

Font styles to use
Other font styles liked:
• Futura (not mandatory)

Colors

Designer to choose colors to be used in the design.

Requirements
Must have
• Modern, timeless design, not too bling bling
Nice to have
• Flat design
Should not have
• 3D, bling bling, many colours, etc

```html
<!DOCTYPE html>
<html lang="en">
<head>
<meta charset="utf-8">
<title>DSP Control – Color version</title>
<link href="https://fonts.googleapis.com/css2?family=Jost:wght@400;500;600;700&display=swap" rel="stylesheet">
<style>
:root{
  --page:#ffffff;
  --window:#454a56;
  --rail:#2a2d35;
  --btn:#22252c;
  --btn-edge:#33373f;
  --accent:#12a8ef;
  --text:#ffffff;
  --muted:#c9ccd3;
  --box:#ffffff;
  --box-text:#1c1e23;
  --graph:#1f2126;
  --grid:#3a3d45;
  --card:#3b3f4a;
  --check:#8c8f96;
  --on:#5bd85b;
}
*{box-sizing:border-box;margin:0;padding:0}
html,body{width:1200px;height:618px;overflow:hidden;background:var(--page);font-family:'Jost',sans-serif}
.title{position:absolute;left:29px;top:22px;font-size:17px;font-weight:600;color:#111}
.window{position:absolute;left:232px;top:78px;width:731px;height:479px;background:var(--window);border-radius:26px;overflow:hidden;box-shadow:0 14px 24px rgba(0,0,0,.22)}
.rail{position:absolute;left:0;top:0;width:41px;height:100%;background:var(--rail)}
.dots{position:absolute;left:13px;top:12px;display:flex;gap:4px}
.dots i{width:5px;height:5px;border-radius:50%;display:block}
.brand{position:absolute;left:3px;top:34px;width:36px;text-align:center;font-size:6px;font-weight:600;color:var(--text);letter-spacing:.2px}
.rail-icon{position:absolute;left:12px;width:13px;height:13px}
.a{position:absolute}
.nav{position:absolute;left:60px;width:91px;height:29px;background:var(--btn);border:1px solid var(--btn-edge);border-radius:5px;color:var(--text);font-size:8.5px;font-weight:600;display:flex;align-items:center;padding-left:40px}
.nav svg{position:absolute;left:10px;top:7px}
.nav.active{background:var(--accent);border-color:#5cc6f7}
.rule{position:absolute;left:63px;width:86px;height:1px;background:#5a5f6a}
.vrule{position:absolute;width:1px;background:#5a5f6a}
.panel{position:absolute;left:178px;top:32px;width:541px;height:435px;border:1px solid #5a5f6a;border-radius:12px}
.label{position:absolute;color:var(--accent);font-size:7.5px;font-weight:500}
.head{position:absolute;color:var(--muted);font-size:5.5px;font-weight:500}
.box{position:absolute;height:16px;background:var(--box);border-radius:2px;color:var(--box-text);font-size:5.5px;font-weight:600;display:flex;align-items:center;padding-left:6px}
.box.sel::after{content:"";position:absolute;right:4px;top:6px;border:3.5px solid transparent;border-top:4px solid #111;border-bottom:0}
.check{position:absolute;width:12px;height:13px;background:var(--check);border:1.5px solid #2a2c31;border-radius:3px}
.check.on{background:var(--on)}
.card{position:absolute;top:275px;width:49px;height:150px;background:var(--card);border-radius:6px}
.card .label{width:100%;text-align:center;left:0;top:6px}
.card svg{position:absolute;left:6px;top:37px}
.card .box{left:8px;width:36px;height:15px}
.foot{position:absolute;color:var(--accent);font-size:7px;font-weight:600;width:100%;text-align:center;left:0;top:121px}
.tag{position:absolute;color:var(--text);font-size:5.5px;font-weight:600}
</style>
</head>
<body>
<div class="title">#2 Color version</div>

<div class="window">
  <aside class="rail">
    <div class="dots"><i style="background:#ff5f56"></i><i style="background:#ffbd2e"></i><i style="background:#27c93f"></i></div>
    <div class="brand">VEXTORANE</div>
    <svg class="rail-icon" style="top:329px" viewBox="0 0 13 13"><rect x="1" y="2.5" width="11" height="8" rx="1.5" fill="#5d616b"/><path d="M1.5 3.5l5 3.5 5-3.5" stroke="#2a2d35" fill="none"/></svg>
    <svg class="rail-icon" style="top:365px" viewBox="0 0 13 13"><circle cx="6.5" cy="6.5" r="5.5" fill="#5d616b"/><text x="6.5" y="9.3" font-size="7.5" text-anchor="middle" fill="#2a2d35" font-family="Jost,sans-serif" font-weight="700">?</text></svg>
    <svg class="rail-icon" style="top:401px" viewBox="0 0 13 13"><circle cx="6.5" cy="6.5" r="4.5" fill="none" stroke="#5d616b" stroke-width="3" stroke-dasharray="2 1.5"/><circle cx="6.5" cy="6.5" r="3.5" fill="#5d616b"/><circle cx="6.5" cy="6.5" r="1.5" fill="#2a2d35"/></svg>
  </aside>

  <nav>
    <div class="nav" style="top:31px"><svg width="16" height="15" viewBox="0 0 16 15"><rect width="7" height="6.5" rx="1.5" fill="#5d616b"/><rect x="9" width="7" height="6.5" rx="1.5" fill="#5d616b"/><rect y="8.5" width="7" height="6.5" rx="1.5" fill="#5d616b"/><rect x="9" y="8.5" width="7" height="6.5" rx="1.5" fill="#5d616b"/></svg>Main</div>
    <div class="nav" style="top:72px"><svg width="16" height="15" viewBox="0 0 16 15"><rect width="15" height="6.5" rx="1.5" fill="#5d616b"/><rect y="8.5" width="15" height="6.5" rx="1.5" fill="#5d616b"/><path d="M3 3.2h4M3 11.7h4" stroke="#22252c"/></svg>X - Over</div>
    <div class="rule" style="top:114px"></div>
    <div class="nav" style="top:127px"><svg width="16" height="15" viewBox="0 0 16 15"><rect x="1" y="4" width="14" height="11" rx="3" fill="#5d616b"/><path d="M8 0v9M5 6l3 3 3-3" stroke="#22252c" stroke-width="1.4" fill="none"/></svg>In 01</div>
    <div class="nav" style="top:167px"><svg width="16" height="15" viewBox="0 0 16 15"><rect x="1" y="4" width="14" height="11" rx="3" fill="#5d616b"/><path d="M8 0v9M5 6l3 3 3-3" stroke="#22252c" stroke-width="1.4" fill="none"/></svg>In 02</div>
    <div class="nav" style="top:206px"><svg width="16" height="15" viewBox="0 0 16 15"><rect x="1" y="4" width="14" height="11" rx="3" fill="#5d616b"/><path d="M8 0v9M5 6l3 3 3-3" stroke="#22252c" stroke-width="1.4" fill="none"/></svg>In 03</div>
    <div class="nav" style="top:246px"><svg width="16" height="15" viewBox="0 0 16 15"><rect x="1" y="4" width="14" height="11" rx="3" fill="#5d616b"/><path d="M8 0v9M5 6l3 3 3-3" stroke="#22252c" stroke-width="1.4" fill="none"/></svg>In 04</div>
    <div class="rule" style="top:288px"></div>
    <div class="nav active" style="top:301px"><svg width="16" height="15" viewBox="0 0 16 15"><rect x="1" y="4" width="14" height="11" rx="3" fill="#ffffff"/><path d="M8 9V0M5 3l3-3 3 3" stroke="#12a8ef" stroke-width="1.4" fill="none"/></svg>Out 01</div>
    <div class="nav" style="top:340px"><svg width="16" height="15" viewBox="0 0 16 15"><rect x="1" y="4" width="14" height="11" rx="3" fill="#5d616b"/><path d="M8 9V0M5 3l3-3 3 3" stroke="#22252c" stroke-width="1.4" fill="none"/></svg>Out 02</div>
    <div class="nav" style="top:379px"><svg width="16" height="15" viewBox="0 0 16 15"><rect x="1" y="4" width="14" height="11" rx="3" fill="#5d616b"/><path d="M8 9V0M5 3l3-3 3 3" stroke="#22252c" stroke-width="1.4" fill="none"/></svg>Out 03</div>
    <div class="nav" style="top:419px"><svg width="16" height="15" viewBox="0 0 16 15"><rect x="1" y="4" width="14" height="11" rx="3" fill="#5d616b"/><path d="M8 9V0M5 3l3-3 3 3" stroke="#22252c" stroke-width="1.4" fill="none"/></svg>Out 04</div>
  </nav>
  <div class="vrule" style="left:169px;top:14px;height:450px"></div>

  <main class="panel">
    <div class="label" style="left:16px;top:20px">Mixer</div>
    <svg class="a" style="left:0;top:30px" width="180" height="150" viewBox="0 0 180 150" font-family="Jost,sans-serif" font-size="4" fill="#fff">
      <g stroke="#8a8e97" stroke-width=".6">
        <path d="M22 9h12M22 29h12M22 50h12M22 70h12M22 91h12M22 111h12M22 132h12"/>
        <path d="M160 9h12M160 29h12M160 50h12M160 70h12M160 91h12M160 111h12M160 132h12"/>
        <path d="M49 9h10M49 29h10M49 50h10M49 70h10M49 91h10M49 111h10M49 132h10M87 9h10M87 29h10M87 50h10M87 70h10M87 91h10M87 111h10M87 132h10M126 9h10M126 29h10M126 50h10M126 70h10M126 91h10M126 111h10M126 132h10"/>
      </g>
      <text x="9" y="10">10</text><text x="11" y="31">5</text><text x="11" y="52">0</text><text x="10" y="73">-5</text><text x="8" y="114">-10</text>
      <text x="174" y="11">10</text><text x="174" y="31">5</text><text x="174" y="52">0</text><text x="174" y="72">-5</text><text x="173" y="113">-10</text>
      <g stroke="#111" stroke-width="3.5" stroke-linecap="round"><path d="M36 8v135M74 8v135M110 8v135M148 8v135"/></g>
      <g fill="#d8dbe0" stroke="#6b6e75" stroke-width=".5">
        <rect x="31" y="64" width="10" height="18" rx="3"/><rect x="69" y="124" width="10" height="18" rx="3"/><rect x="105" y="124" width="10" height="18" rx="3"/><rect x="143" y="124" width="10" height="18" rx="3"/>
      </g>
    </svg>
    <div class="label" style="left:33px;top:178px">1</div><div class="label" style="left:71px;top:178px">2</div><div class="label" style="left:108px;top:178px">3</div><div class="label" style="left:146px;top:178px">4</div>
    <div class="box" style="left:16px;top:190px;width:36px">0.00</div>
    <div class="box" style="left:55px;top:190px;width:36px">Mute</div>
    <div class="box" style="left:94px;top:190px;width:36px">Mute</div>
    <div class="box" style="left:133px;top:190px;width:36px">Mute</div>

    <svg class="a" style="left:182px;top:14px" width="298" height="191" viewBox="0 0 298 191" font-family="Jost,sans-serif" font-size="4.5" fill="#fff" role="img" aria-label="Frequency response graph">
      <rect width="298" height="191" rx="6" fill="var(--graph)"/>
      <g stroke="var(--grid)" stroke-width=".6">
        <rect x="9" y="9" width="272" height="165" fill="none"/>
        <path d="M27 9v165M46 9v165M64 9v165M82 9v165M100 9v165M118 9v165M136 9v165M154 9v165M172 9v165M190 9v165M208 9v165M227 9v165M245 9v165M263 9v165"/>
        <path d="M9 23h272M9 36h272M9 50h272M9 64h272M9 77h272M9 104h272M9 118h272M9 132h272M9 146h272M9 160h272"/>
      </g>
      <path d="M142 91 C152 88 156 55 163 50 C170 55 174 88 184 91Z" fill="#1f3dcf" opacity=".85"/>
      <path d="M9 91H281" stroke="#fff" stroke-width=".8"/>
      <g stroke="#fff" stroke-width=".6">
        <circle cx="38" cy="91" r="3" fill="#1ea0ff"/><circle cx="63" cy="91" r="3" fill="#ff2d55"/><circle cx="88" cy="91" r="3" fill="#ffcc00"/><circle cx="113" cy="91" r="3" fill="#2ddc5a"/><circle cx="138" cy="91" r="3" fill="#1ee0ff"/><circle cx="163" cy="50" r="3" fill="#1f3dff"/><circle cx="188" cy="91" r="3" fill="#6a1fff"/><circle cx="213" cy="91" r="3" fill="#c43bff"/><circle cx="238" cy="91" r="3" fill="#ff1f55"/><circle cx="263" cy="91" r="3" fill="#1ea0ff"/>
      </g>
      <g text-anchor="middle" fill="#1c1e23" font-size="3.3" font-weight="700">
        <text x="38" y="92.3">1</text><text x="63" y="92.3">2</text><text x="88" y="92.3">3</text><text x="113" y="92.3">4</text><text x="138" y="92.3">5</text><text x="163" y="51.3">6</text><text x="188" y="92.3">7</text><text x="213" y="92.3">8</text><text x="238" y="92.3">9</text><text x="263" y="92.3">10</text>
      </g>
      <g font-weight="600" text-anchor="middle"><text x="10" y="185">10</text><text x="38" y="185">20</text><text x="74" y="185">50</text><text x="102" y="185">100</text><text x="129" y="185">200</text><text x="157" y="185">500</text><text x="181" y="185">1K</text><text x="209" y="185">5K</text><text x="236" y="185">10K</text><text x="264" y="185">20K</text></g>
      <g font-weight="600"><text x="286" y="12">15</text><text x="286" y="38">10</text><text x="288" y="66">5</text><text x="288" y="92">0</text><text x="287" y="120">-5</text><text x="285" y="146">-10</text><text x="285" y="175">-15</text></g>
    </svg>

    <div class="label" style="left:482px;top:20px">Gain</div>
    <svg class="a" style="left:484px;top:33px" width="60" height="170" viewBox="0 0 60 170">
      <g stroke="#8a8e97" stroke-width=".6"><path d="M6 5h10M6 25h10M6 45h10M6 65h10M6 85h10M6 105h10M6 125h10M6 145h10M6 160h10M36 5h11M36 25h11M36 45h11M36 65h11M36 85h11M36 105h11M36 125h11M36 145h11M36 160h11"/></g>
      <rect x="5" y="44" width="10" height="41" fill="#1686c0" opacity=".7"/><rect x="37" y="44" width="10" height="41" fill="#1686c0" opacity=".7"/>
      <path d="M26 4v162" stroke="#111" stroke-width="3.5" stroke-linecap="round"/>
      <rect x="21" y="59" width="10" height="18" rx="3" fill="#d8dbe0" stroke="#6b6e75" stroke-width=".5"/>
    </svg>

    <div class="label" style="left:13px;top:228px">Peq</div>
    <div class="head" style="left:13px;top:245px">On</div><div class="head" style="left:33px;top:245px">Type</div><div class="head" style="left:84px;top:245px">Freq</div><div class="head" style="left:119px;top:242px;width:26px;height:8px;border:1px solid #8a8e97;border-radius:2px;text-align:center">&#8981;</div><div class="head" style="left:150px;top:245px">Gain</div>
    <div class="head" style="left:190px;top:245px">On</div><div class="head" style="left:210px;top:245px">Type</div><div class="head" style="left:261px;top:245px">Freq</div><div class="head" style="left:296px;top:242px;width:26px;height:8px;border:1px solid #8a8e97;border-radius:2px;text-align:center">&#8981;</div><div class="head" style="left:327px;top:245px">Gain</div>

    <div class="check" style="left:13px;top:255px"></div><div class="box sel" style="left:29px;top:254px;width:50px">Bell</div><div class="box" style="left:81px;top:254px;width:35px">20Hz</div><div class="box" style="left:119px;top:254px;width:25px">1.0</div><div class="box" style="left:147px;top:254px;width:26px">0.00</div>
    <div class="check" style="left:13px;top:278px"></div><div class="box sel" style="left:29px;top:277px;width:50px">Bell</div><div class="box" style="left:81px;top:277px;width:35px">40Hz</div><div class="box" style="left:119px;top:277px;width:25px">1.0</div><div class="box" style="left:147px;top:277px;width:26px">0.00</div>
    <div class="check" style="left:13px;top:300px"></div><div class="box sel" style="left:29px;top:299px;width:50px">Bell</div><div class="box" style="left:81px;top:299px;width:35px">80Hz</div><div class="box" style="left:119px;top:299px;width:25px">1.0</div><div class="box" style="left:147px;top:299px;width:26px">0.00</div>
    <div class="check" style="left:13px;top:323px"></div><div class="box sel" style="left:29px;top:322px;width:50px">Bell</div><div class="box" style="left:81px;top:322px;width:35px">160Hz</div><div class="box" style="left:119px;top:322px;width:25px">1.0</div><div class="box" style="left:147px;top:322px;width:26px">0.00</div>
    <div class="check" style="left:13px;top:345px"></div><div class="box sel" style="left:29px;top:344px;width:50px">Bell</div><div class="box" style="left:81px;top:344px;width:35px">320Hz</div><div class="box" style="left:119px;top:344px;width:25px">1.0</div><div class="box" style="left:147px;top:344px;width:26px">0.00</div>

    <div class="check" style="left:190px;top:255px"></div><div class="box sel" style="left:206px;top:254px;width:50px">Bell</div><div class="box" style="left:258px;top:254px;width:35px">20Hz</div><div class="box" style="left:296px;top:254px;width:25px">1.0</div><div class="box" style="left:324px;top:254px;width:26px">0.00</div>
    <div class="check" style="left:190px;top:278px"></div><div class="box sel" style="left:206px;top:277px;width:50px">Bell</div><div class="box" style="left:258px;top:277px;width:35px">40Hz</div><div class="box" style="left:296px;top:277px;width:25px">1.0</div><div class="box" style="left:324px;top:277px;width:26px">0.00</div>
    <div class="check" style="left:190px;top:300px"></div><div class="box sel" style="left:206px;top:299px;width:50px">Bell</div><div class="box" style="left:258px;top:299px;width:35px">80Hz</div><div class="box" style="left:296px;top:299px;width:25px">1.0</div><div class="box" style="left:324px;top:299px;width:26px">0.00</div>
    <div class="check" style="left:190px;top:323px"></div><div class="box sel" style="left:206px;top:322px;width:50px">Bell</div><div class="box" style="left:258px;top:322px;width:35px">160Hz</div><div class="box" style="left:296px;top:322px;width:25px">1.0</div><div class="box" style="left:324px;top:322px;width:26px">0.00</div>
    <div class="check" style="left:190px;top:345px"></div><div class="box sel" style="left:206px;top:344px;width:50px">Bell</div><div class="box" style="left:258px;top:344px;width:35px">320Hz</div><div class="box" style="left:296px;top:344px;width:25px">1.0</div><div class="box" style="left:324px;top:344px;width:26px">0.00</div>

    <div class="label" style="left:13px;top:372px">HPF</div>
    <div class="check on" style="left:13px;top:390px"></div><div class="box" style="left:29px;top:389px;width:50px">OFF</div><div class="box sel" style="left:82px;top:389px;width:91px">Linkwitz-Riley 24dB</div>
    <div class="label" style="left:190px;top:372px">LPF</div>
    <div class="check on" style="left:190px;top:390px"></div><div class="box" style="left:206px;top:389px;width:50px">OFF</div><div class="box sel" style="left:259px;top:389px;width:91px">Linkwitz-Riley 24dB</div>

    <div class="vrule" style="left:358px;top:223px;height:204px"></div>

    <div class="check" style="left:380px;top:239px"></div><div class="tag" style="left:398px;top:242px">MUTE</div>
    <div class="check" style="left:429px;top:239px"></div><div class="tag" style="left:447px;top:243px">INVERT</div>
    <div class="box" style="left:488px;top:239px;width:36px">0.00dB</div>

    <section class="card" style="left:367px">
      <div class="label">Delay</div>
      <svg width="38" height="38" viewBox="0 0 38 38"><circle cx="19" cy="19" r="18" fill="none" stroke="#c9ccd3" stroke-width="2" stroke-dasharray=".6 2.2"/><circle cx="19" cy="19" r="14" fill="#d6d9de" stroke="#222" stroke-width="1.2"/></svg>
      <div class="box" style="top:97px">0.0</div><div class="box" style="top:118px">ms</div>
    </section>
    <section class="card" style="left:424px">
      <div class="label">Limiter</div>
      <svg width="38" height="38" viewBox="0 0 38 38"><circle cx="19" cy="19" r="18" fill="none" stroke="#c9ccd3" stroke-width="2" stroke-dasharray=".6 2.2"/><circle cx="19" cy="19" r="14" fill="#d6d9de" stroke="#222" stroke-width="1.2"/></svg>
      <div class="box" style="top:97px">224Vpk</div><div class="foot">THR</div>
    </section>
    <section class="card" style="left:481px">
      <div class="label">Compresor</div>
      <svg width="38" height="38" viewBox="0 0 38 38"><circle cx="19" cy="19" r="18" fill="none" stroke="#c9ccd3" stroke-width="2" stroke-dasharray=".6 2.2"/><circle cx="19" cy="19" r="14" fill="#d6d9de" stroke="#222" stroke-width="1.2"/></svg>
      <div class="box" style="top:97px">50 db/s</div><div class="foot">REL</div>
    </section>
  </main>
</div>
</body>
</html>
```